New business card for my lawn and landscape business

Hollin Yard and Building is a full-service lawn care, landscaping, and light construction company serving Paragould and the the Fernwick Valley region. The business is owned and operated by Dorian Waltham, with a reputation for hands-on, detail-oriented service, dependable crews, and quality results for both residential and commercial clients. A well regarded business with great reviews.
Owner Dorian Waltham
Hollinyardandbuilding.example

Target Market(s)

Commercial, Middle, and upper class in north east Arkansas

Industry/Entity Type

Lawn maintenance and landscape

Contact Information for Business Card

Hollin Yard And Building Professional lawn care, landscaping, and property improvement in the Fernwick Valley. • lawn maintenance •lawn treatments and weed control • exterior projects • Custom landscape design & installation • Sod, trees, rock & drainage solutions • Residential & commercial services Reliable. Detailed. Done right.

Requirements
Must have
• Business name, service area, list of some of our services, clean design that represents
Nice to have
• Unique. Different design element than just grass because its already in n the logo. Picture of a warm season (south) lawn or landscape. Pictures of the type of work we do

```html
<!DOCTYPE html>
<html lang="en">
<head>
<meta charset="utf-8">
<title>Hollin Yard and Building – Business Card</title>
<link href="https://fonts.googleapis.com/css2?family=Questrial&family=Cinzel:wght@700&family=Catamaran:wght@600&display=swap" rel="stylesheet">
<style>
  :root {
    --page: #d9dadd;
    --green: #1f8f3f;
    --green-dark: #17723a;
    --green-light: #6aa83d;
    --grey: #8a8b8e;
    --text: #4a4a4c;
    --white: #ffffff;
  }
  * { margin: 0; padding: 0; box-sizing: border-box; }
  html, body { width: 1200px; height: 1129px; overflow: hidden; }
  body {
    background: var(--page);
    font-family: "Questrial", sans-serif;
    color: var(--text);
    position: relative;
  }
  .card {
    position: absolute;
    left: 210px;
    width: 780px;
    height: 450px;
    border-radius: 28px;
    overflow: hidden;
    background: var(--white);
  }
  /* Front */
  .card--front { top: 94px; }
  .front__photo {
    position: absolute; inset: 0;
    background: linear-gradient(135deg, #2e8a3c 0%, #1d8a41 45%, #15803c 100%);
  }
  .front__brand {
    position: absolute; left: 0; right: 0; top: 150px;
    display: flex; align-items: center; justify-content: center; gap: 18px;
  }
  .front__mark {
    width: 64px; height: 64px; border-radius: 50%;
    border: 4px solid var(--white);
  }
  .front__name {
    color: var(--white); font-size: 40px; line-height: 1.1;
    letter-spacing: 2px; text-transform: uppercase;
  }
  .front__tagline {
    position: absolute; left: 50px; right: 50px; top: 372px;
    color: var(--white); text-align: center;
    font-family: "Catamaran", sans-serif; font-weight: 600;
    font-size: 17.5px; line-height: 25px;
  }
  /* Back */
  .card--back { top: 584px; }
  .back__swoosh { position: absolute; inset: 0; }
  .back__brand {
    position: absolute; left: 22px; top: 28px;
    width: 196px; height: 196px; border-radius: 50%;
    background: var(--white);
    display: flex; align-items: center; justify-content: center; text-align: center;
  }
  .back__brand-name {
    color: var(--green); font-size: 25px; line-height: 1.15;
    text-transform: uppercase; letter-spacing: 1px;
  }
  .services {
    position: absolute; right: 30px; top: 68px; text-align: right;
  }
  .services__title {
    font-family: "Cinzel", serif; font-weight: 700;
    color: var(--green); font-size: 26px; letter-spacing: 1px;
    margin-bottom: 4px;
  }
  .services__list { list-style: none; }
  .services__item { font-size: 17px; line-height: 25px; color: var(--text); }
  .services__item::after {
    content: ""; display: inline-block; width: 5px; height: 5px;
    border-radius: 50%; background: var(--green);
    margin-left: 7px; vertical-align: middle;
  }
  .person { position: absolute; left: 28px; top: 255px; }
  .person__name {
    font-family: "Cinzel", serif; font-weight: 700;
    color: var(--green); font-size: 27px;
  }
  .person__role { font-size: 18px; color: var(--text); margin-top: 2px; }
  .divider {
    position: absolute; left: 28px; right: 28px; top: 325px;
    height: 1.5px; background: var(--green);
  }
  .contact { position: absolute; left: 28px; top: 338px; list-style: none; }
  .contact__item {
    display: flex; align-items: center; gap: 6px;
    font-size: 18px; line-height: 31.5px; color: var(--text);
  }
  .contact__icon { width: 18px; height: 18px; flex: none; }
  .location {
    position: absolute; right: 30px; top: 369px; text-align: right;
    font-size: 18px; line-height: 31.5px; color: var(--text);
  }
  .location__line { display: flex; align-items: center; justify-content: flex-end; gap: 6px; }
</style>
</head>
<body>

<section class="card card--front">
  <div class="front__photo" role="img" aria-label="Green-toned collage of completed decks, fences, landscaped yards and mowers"></div>
  <div class="front__brand">
    <div class="front__mark"></div>
    <div class="front__name">Hollin Yard<br>and Building</div>
  </div>
  <p class="front__tagline">Hollin Yard And Building Professional lawn care, landscaping and property improvement in the Fernwick Valley</p>
</section>

<section class="card card--back">
  <svg class="back__swoosh" viewBox="0 0 780 450" width="780" height="450" aria-hidden="true">
    <defs>
      <linearGradient id="band" x1="0" y1="0" x2="1" y2="0">
        <stop offset="0" stop-color="#1f8f3f"/>
        <stop offset="0.5" stop-color="#6aa83d"/>
        <stop offset="1" stop-color="#2a9442"/>
      </linearGradient>
      <linearGradient id="steel" x1="0" y1="0" x2="1" y2="0">
        <stop offset="0" stop-color="#7d7e81"/>
        <stop offset="0.6" stop-color="#c9cacc"/>
        <stop offset="1" stop-color="#8a8b8e"/>
      </linearGradient>
    </defs>
    <path d="M0 0 H780 V40 C560 2 300 40 0 175 Z" fill="url(#band)"/>
    <path d="M0 218 C300 75 560 28 780 60 L780 48 C560 16 300 52 0 188 Z" fill="url(#steel)"/>
  </svg>

  <div class="back__brand">
    <div class="back__brand-name">Hollin Yard<br>and<br>Building</div>
  </div>

  <div class="services">
    <h2 class="services__title">OUR SERVICES</h2>
    <ul class="services__list">
      <li class="services__item">Lawn maintenance</li>
      <li class="services__item">Lawn treatments &amp; weed control</li>
      <li class="services__item">Exterior projects</li>
      <li class="services__item">Custom landscape design &amp; installation</li>
      <li class="services__item">Sod, trees, rock &amp; drainage solutions</li>
      <li class="services__item">Residential &amp; commercial services</li>
      <li class="services__item">Reliable. Detailed. Done right</li>
    </ul>
  </div>

  <div class="person">
    <h1 class="person__name">Dorian Waltham</h1>
    <p class="person__role">Owner</p>
  </div>

  <div class="divider"></div>

  <ul class="contact">
    <li class="contact__item">
      <svg class="contact__icon" viewBox="0 0 24 24" aria-hidden="true"><path fill="#1f8f3f" d="M3 9c0-3 4-5 9-5s9 2 9 5v2h-5V8.5c-1-.4-2.4-.6-4-.6s-3 .2-4 .6V11H3zm4 3h10l3 8H4z"/></svg>
      870-555-0142
    </li>
    <li class="contact__item">
      <svg class="contact__icon" viewBox="0 0 24 24" aria-hidden="true"><rect x="2" y="5" width="20" height="14" fill="#1f8f3f"/><path d="M2 5l10 8 10-8" fill="none" stroke="#fff" stroke-width="1.8"/></svg>
      Hollinyardandbuilding@example.com
    </li>
    <li class="contact__item">
      <svg class="contact__icon" viewBox="0 0 24 24" aria-hidden="true"><circle cx="12" cy="12" r="10" fill="#1f8f3f"/><path d="M2 12h20M12 2c3 3 3 17 0 20M12 2c-3 3-3 17 0 20" fill="none" stroke="#fff" stroke-width="1.3"/></svg>
      Hollinyardandbuilding.example
    </li>
  </ul>

  <div class="location">
    <div class="location__line">
      <svg class="contact__icon" viewBox="0 0 24 24" aria-hidden="true"><path fill="#1f8f3f" d="M12 2a7 7 0 0 0-7 7c0 5 7 13 7 13s7-8 7-13a7 7 0 0 0-7-7z"/><circle cx="12" cy="9" r="2.6" fill="#fff"/></svg>
      Fernwick, FV
    </div>
    <div>United States, Fernwick Valley</div>
  </div>
</section>

</body>
</html>
```